Company profile urgent

Hi, I had my designer fail to deliver and I am looking for urgent designers job. Needs to go to print tomorrow the latest. I need company profile designed and finished, I do have a start of the project but did not like the overall design as it was too simple and not something I would asking for. This needs to be a great job and we are willing to pay for the right job.

This is pretty much a folded brochure as you will see from the document that is attached. On the front side do not remove LOGO from the actual position as it must stay there for the purposes of the cover that is going over and it has a whole for the logo where it is. Also, the pages are set as it should be so do not change the order of the pages, only the design, feel and look. This is for a travel company needs to look expensive, upscale, vip and must have clean design.

Needs to be done:

.

Needs to be done:

1) Get the design more attractive and modern. Not looking for cheap but high quality material.
2) As you can see we are tryin to present 4 products in the brochure that we do and this will be a folded brochure.
3) Infographics, especially the table ''when to travel'' needs updates and more style
4) This design is very steril, we are looking for clean and modern design
5) On the front page add Company profile text somewhere and add any design on home page is welcome BUT logo must stay where is
6) Please send final print ready documents as well as editable so we can move the logo if needed as it must fit the whole on a brochure holder
7) Last page with contacts very poorly done by my designer, needs upgrade with maybe infographics for phone, email web etc... ideas welcome
8) if you need more photos at the end is link to photo bank

Ideas welcome! Again we need it fast and clean.

Photo bank:
https://files.example-share.net/f/q7Rm2LpX9vKt3NwB_hYe-uD4cZa-

Designes that we linked: https://layoutbazaar.example/item/company-profile-square-brochure/58203716?s_rank=8
https://layoutbazaar.example/item/company-profile_square/61937204?s_rank=32
https://layoutbazaar.example/item/square-brochure/64710392?s_rank=52

This is our webiste so you get the feeling of the colors: www.tramont-journeys.example

Important: Do not change text, or change pages, everything is as it should be just needs upgradede design! Logo on the first page must stay on the position as is.

Photo bank:

Target Market(s)

We are travel supplier targeting travel agents and travel companies

Industry/Entity Type

Travel Industry

Font styles to use
Serif
Sans Serif

Requirements
Must have
• https://files.example-share.net/f/q7Rm2LpX9vKt8pH_D3muWE5QbTokzr
Nice to have
• Cool design: https://layoutbazaar.example/item/business-solution-brochure-template/57382910?s_rank=3
• Cool design 2: https://layoutbazaar.example/item/travel-agency-catalog-brochure/57491836?s_rank=6
Should not have
• Do not change the dimensions. You have the design attached, indd file. Needs work and update.

```html
<!DOCTYPE html>
<html lang="en">
<head>
<meta charset="utf-8">
<title>Tramont Tours – Company Profile Brochure</title>
<link rel="stylesheet" href="https://fonts.googleapis.com/css2?family=Montserrat:wght@600;800;900&family=Quicksand:wght@300;400;500&display=swap">
<style>
:root{
  --backdrop:#d6d6d6;
  --crimson:#a30f24;
  --crimson-deep:#7d0b1b;
  --crimson-dark:#5e0814;
  --paper:#ffffff;
  --sky:#9fc3e0;
  --ink-red:#b0122a;
  --body-font:'Quicksand',sans-serif;
  --head-font:'Montserrat',sans-serif;
}
*{box-sizing:border-box;margin:0;padding:0}
html,body{width:1200px;height:1200px;overflow:hidden;background:var(--backdrop);font-family:var(--body-font)}
.canvas{position:relative;width:1200px;height:1200px;overflow:hidden}

/* ---------- top spread ---------- */
.spread-outer{position:absolute;left:0;top:21px;width:1117px;height:567px;box-shadow:0 4px 10px rgba(0,0,0,.25)}
.panel-back{position:absolute;left:0;top:0;width:548px;height:567px;overflow:hidden;
  background:linear-gradient(160deg,#c83a3a 0%,var(--crimson) 35%,#b8553c 55%,#8a1a22 75%,#5f8aa0 100%)}
.map-shape{position:absolute;inset:0}
.when-box{position:absolute;left:16px;top:367px;width:498px;height:188px;background:rgba(150,12,30,.88)}
.trip-badge{position:absolute;left:56px;top:333px;width:70px;height:70px}
.when-table{position:absolute;left:28px;top:420px;border-collapse:collapse;color:#fff;font-family:var(--head-font)}
.when-table th,.when-table td{border:1px solid rgba(255,255,255,.75);height:28px;text-align:center;font-size:9px;font-weight:600}
.when-table th.label,.when-table td.label{border:none;text-align:left;width:114px;font-size:11.5px;padding-left:4px}
.when-table th.label{font-weight:800;font-size:11px}
.when-table td.label{border-top:1px solid rgba(255,255,255,.6);border-bottom:1px solid rgba(255,255,255,.6);font-weight:600}
.when-table th.m,.when-table td.r{width:29.2px}
.rating{display:inline-block;width:17px;height:17px;border:1.3px solid #fff;border-radius:50%;vertical-align:middle}
.rating.good{background:#fff}
.rating.fair{background:linear-gradient(90deg,#fff 50%,transparent 50%)}
.row-icon{display:inline-block;width:16px;height:16px;border:1px solid #fff;border-radius:50%;vertical-align:middle;margin-right:4px}

.panel-cover{position:absolute;left:548px;top:0;width:569px;height:567px}
.cover-top{position:absolute;left:0;top:0;width:569px;height:285px;background:var(--paper)}
.brand{position:absolute;left:0;top:98px;width:569px;text-align:center;color:var(--crimson);font-family:var(--head-font);font-weight:900}
.brand-name{font-size:64px;letter-spacing:2px;line-height:1}
.brand-sub{font-size:18px;letter-spacing:56px;margin-top:26px;padding-left:56px;line-height:1}
.cover-bottom{position:absolute;left:0;top:285px;width:569px;height:282px;
  background:linear-gradient(180deg,#8c1222 0%,var(--crimson-deep) 60%,var(--crimson-dark) 100%)}
.cover-title{position:absolute;left:0;top:96px;width:569px;text-align:center;font-family:var(--head-font);font-size:78px;font-weight:900;letter-spacing:-1px;line-height:1;
  background:linear-gradient(180deg,var(--sky) 0%,#e7d2b4 55%,#d9703d 100%);-webkit-background-clip:text;background-clip:text;color:transparent}
.cover-tagline{position:absolute;left:0;top:182px;width:569px;text-align:center;color:#fff;font-size:20px;font-weight:400}

/* ---------- bottom spread ---------- */
.spread-inner{position:absolute;left:79px;top:608px;width:1121px;height:576px;box-shadow:0 4px 10px rgba(0,0,0,.25);overflow:hidden}
.edge-strip{position:absolute;left:0;top:0;width:9px;height:576px;background:var(--crimson)}
.page-intro{position:absolute;left:9px;top:0;width:308px;height:576px;background:var(--paper)}
.page-intro .corner{position:absolute;right:0;bottom:0;width:25px;height:27px;background:var(--crimson)}
.heading{color:var(--ink-red);font-family:var(--head-font);font-weight:800;font-size:17px;line-height:23px}
.copy{color:var(--ink-red);font-weight:400;font-size:11.4px;line-height:14.6px}
.intro-block{position:absolute;left:30px;top:40px;width:246px}
.intro-block .copy{margin-top:15px;text-align:justify;text-align-last:left}
.intro-block .features{margin-top:14px}
.intro-block .features p{text-align:justify;text-align-last:left}

.photo-harbour{position:absolute;left:317px;top:0;width:730px;height:576px;
  background:linear-gradient(135deg,#1b4f86 0%,#2a6aa3 30%,#c7b9a6 48%,#d2693a 60%,#b9b2a6 72%,#3f6f3a 100%)}
.group-box{position:absolute;left:721px;top:72px;width:282px;height:424px;background:rgba(255,255,255,.93);border-bottom:4px solid var(--crimson);padding:22px 20px 0 21px}
.group-box .copy{margin-top:18px}
.group-box ul{list-style:none;margin-top:14px}
.group-box li{color:var(--ink-red);font-weight:400;font-size:11.4px;line-height:14.6px;margin-bottom:14px;padding-left:8px;text-indent:-6px}
.group-box li::before{content:"• "}

.page-about{position:absolute;left:1047px;top:0;width:80px;height:576px;overflow:hidden;
  background:linear-gradient(180deg,var(--crimson-deep),var(--crimson) 50%,var(--crimson-deep))}
.about-inner{position:absolute;left:32px;top:52px;width:240px;color:#fff}
.about-inner .heading{color:#fff;font-size:22px;line-height:29px}
.about-inner .copy{color:rgba(255,255,255,.85);margin-top:20px;width:240px}
.about-inner .copy + .copy{margin-top:14px}
</style>
</head>
<body>
<div class="canvas">

  <section class="spread-outer">
    <div class="panel-back">
      <div class="map-shape" role="img" aria-label="Photo of a Croatian old town with red rooftops and coastline, overlaid with a crimson map of the region and a location pin on Croatia"></div>
      <svg style="position:absolute;left:373px;top:116px" width="52" height="66" viewBox="0 0 52 66" aria-hidden="true">
        <path d="M26 2C13 2 3 12 3 25c0 17 23 39 23 39s23-22 23-39C49 12 39 2 26 2z" fill="#fff"/>
        <circle cx="26" cy="25" r="12" fill="var(--crimson)"/>
      </svg>
      <div class="when-box"></div>
      <svg class="trip-badge" viewBox="0 0 70 70" aria-hidden="true">
        <circle cx="35" cy="35" r="33" fill="var(--crimson-deep)" stroke="#fff" stroke-width="1.5"/>
        <rect x="22" y="28" width="26" height="26" rx="3" fill="#fff"/>
        <path d="M29 28v-6h12v6" fill="none" stroke="#fff" stroke-width="2.5"/>
        <path d="M18 12l10 3" stroke="#fff" stroke-width="2"/>
      </svg>
      <table class="when-table">
        <tr><th class="label">WHEN TO GO?</th><th class="m">JAN</th><th class="m">FEB</th><th class="m">MAR</th><th class="m">APR</th><th class="m">MAY</th><th class="m">JUN</th><th class="m">JUL</th><th class="m">AUG</th><th class="m">SEP</th><th class="m">OCT</th><th class="m">NOV</th><th class="m">DEC</th></tr>
        <tr><td class="label"><span class="row-icon"></span>WEATHER</td>
          <td class="r"><span class="rating"></span></td><td class="r"><span class="rating"></span></td><td class="r"><span class="rating fair"></span></td><td class="r"><span class="rating good"></span></td><td class="r"><span class="rating good"></span></td><td class="r"><span class="rating good"></span></td><td class="r"><span class="rating good"></span></td><td class="r"><span class="rating good"></span></td><td class="r"><span class="rating good"></span></td><td class="r"><span class="rating fair"></span></td><td class="r"><span class="rating"></span></td><td class="r"><span class="rating"></span></td></tr>
        <tr><td class="label"><span class="row-icon"></span>CROWDS</td>
          <td class="r"><span class="rating good"></span></td><td class="r"><span class="rating good"></span></td><td class="r"><span class="rating good"></span></td><td class="r"><span class="rating good"></span></td><td class="r"><span class="rating good"></span></td><td class="r"><span class="rating fair"></span></td><td class="r"><span class="rating"></span></td><td class="r"><span class="rating"></span></td><td class="r"><span class="rating fair"></span></td><td class="r"><span class="rating good"></span></td><td class="r"><span class="rating good"></span></td><td class="r"><span class="rating good"></span></td></tr>
        <tr><td class="label"><span class="row-icon"></span>PRICES</td>
          <td class="r"><span class="rating good"></span></td><td class="r"><span class="rating good"></span></td><td class="r"><span class="rating good"></span></td><td class="r"><span class="rating good"></span></td><td class="r"><span class="rating fair"></span></td><td class="r"><span class="rating fair"></span></td><td class="r"><span class="rating"></span></td><td class="r"><span class="rating"></span></td><td class="r"><span class="rating fair"></span></td><td class="r"><span class="rating good"></span></td><td class="r"><span class="rating good"></span></td><td class="r"><span class="rating good"></span></td></tr>
      </table>
    </div>

    <div class="panel-cover">
      <div class="cover-top">
        <div class="brand">
          <div class="brand-name">TRAMONT</div>
          <div class="brand-sub">TOURS</div>
        </div>
      </div>
      <div class="cover-bottom" role="img" aria-label="Crimson-toned photo of an old town skyline with a church dome">
        <div class="cover-title">CROATIA</div>
        <div class="cover-tagline">We Live it. You'll Love it.</div>
      </div>
    </div>
  </section>

  <section class="spread-inner">
    <div class="edge-strip"></div>
    <div class="page-intro">
      <div class="intro-block">
        <h2 class="heading">CUSTOMIZED TRIPS THROUGHOUT CROATIA AND EASTERN EUROPE</h2>
        <p class="copy">We create exceptional, customized itineraries via our front line team of local experts, many of whom call Croatia home and are wonderfully experienced in the destinations Tramont Journeys sells. Our sales representatives are consistently living the destinations, and receive constant education to ensure they are up to date on product news, trends and discoveries which will ensure you have the best information at your fingertips to recommend to your clients.</p>
        <div class="copy features">
          <p>Itineraries crafted to perfection according to your client's interests and preferences</p>
          <p>Fast turnaround and guaranteed 48H delivery</p>
          <p>Unlimited revisions at no cost</p>
          <p>Wide selection of handpicked high-end accommodations including hotels and private villas</p>
          <p>Only selling tours that our team has experienced personally</p>
          <p>Licensed and In-house trained guides for all excursions and transfers</p>
          <p>Private transfers and chauffeur service available in a variety of vehicles</p>
          <p>Combined luxury land and boating itineraries</p>
          <p>Shore trips: Our team customizes private daily trips for your cruise clients visiting Croatia, Slovenia, and Montenegro.</p>
        </div>
      </div>
      <div class="corner"></div>
    </div>

    <div class="photo-harbour" role="img" aria-label="Aerial photo of a walled old town with orange rooftops, a fortress and a harbour with boats on deep blue sea"></div>

    <div class="group-box">
      <h2 class="heading">SMALL GROUP TOURS TO CROATIA AND EASTERN EUROPE</h2>
      <p class="copy">Work with our team of local destination group experts to develop the finest programs for 10 pax or more. &nbsp;Our group specialists have all the experience to be able to work with you and create perfectly balanced itineraries and agendas to meet your group's pace, activity level and interests.</p>
      <ul>
        <li>Exclusive group itineraries designed to meet the way your group travels</li>
        <li>Special booking conditions for added values, and 1 traveler free on every 15th traveler</li>
        <li>Group rates available Use of only high class coaches</li>
        <li>Combination of land and sea options available</li>
      </ul>
    </div>

    <div class="page-about">
      <div class="about-inner">
        <h2 class="heading">ABOUT<br>CROATIA</h2>
        <p class="copy">Since 2008 we have been crafting bespoke journeys in Croatia, Slovenia, Montenegro and Bosnia. Tramont Journeys Tours is proud to offer good value to every traveler, and our team is focused on giving each traveler the best service, guides and drivers, with the options they need.</p>
        <p class="copy">Our mission is to take the stress out of the planning for discerning travelers of all walks of life, testing every service on the ground, and pre-checking something new so you have a partner that cares for you and everything you can offer.</p>
      </div>
    </div>
  </section>

</div>
</body>
</html>
```